Ledgerwell Capital Partners Deck & Brochure

Have a PPT deck and a two page PDF "brochure" that we have to give to clients. Content is there but it could REALLY use some punching up. Including both here because they need to be similar in look and feel

Our website is www.ledgerwellcapitalpartners.example to get a feel for our "design style" so far, including our logo.

Also have a video at video.ledgerwellcapitalpartners.example

Target Market(s)

Large and medium sized corporations, typically a Treasurer

Industry/Entity Type

Management

Requirements
Nice to have
• Movement or animation in the slides of the PPT
Transitions between slides would be nice but it can't be too sassy or take too long

```html
<!DOCTYPE html>
<html lang="en">
<head>
<meta charset="utf-8">
<title>Ledgerwell Capital Partners – Deck Slides</title>
<link rel="stylesheet" href="https://fonts.googleapis.com/css2?family=PT+Sans:wght@400;700&family=Tinos:ital,wght@0,400;1,400;1,700&family=Bree+Serif&display=swap">
<style>
:root{
  --navy:#1b2456;
  --gold:#a8894e;
  --gold-dark:#8f7440;
  --grey:#6b6b6b;
  --rule:#cfcfd6;
  --paper:#ffffff;
  --stage:#c98d52;
}
*{box-sizing:border-box;margin:0;padding:0}
html,body{width:1200px;height:926px;overflow:hidden}
body{background:var(--stage);position:relative;font-family:"PT Sans",sans-serif;color:var(--navy)}
.slide{position:absolute;width:318px;height:238px;background:var(--paper);overflow:hidden;box-shadow:0 2px 5px rgba(0,0,0,.25)}
.slide-footer{position:absolute;left:0;bottom:0;width:318px;height:26px}
.slide-footer svg{position:absolute;left:0;top:0}
.footer-note{position:absolute;right:14px;bottom:3px;font:italic 700 6px "Tinos",serif;color:#fff;letter-spacing:.2px}
.cover .footer-note{font-size:7.5px;bottom:2px}
.slide-title{position:absolute;font-weight:700;font-size:14.5px;color:var(--navy)}
/* cover */
.brand{position:absolute;font-family:"Tinos",serif;color:var(--navy);font-size:17px;line-height:1.05;letter-spacing:.3px}
.cover-title{position:absolute;right:48px;top:130px;text-align:right;font:italic 400 17px "Tinos",serif;color:var(--navy)}
.cover-amp{position:absolute;right:48px;top:148px;font:italic 400 36px "Tinos",serif;color:var(--gold)}
.cover-sub{position:absolute;right:48px;top:186px;font:italic 400 12.5px "Tinos",serif;color:var(--navy)}
/* lists */
.contents{position:absolute;left:50px;top:70px;list-style:none}
.contents li{font-size:7px;font-weight:700;margin-bottom:7.2px;padding-left:10px;position:relative}
.contents li::before,.toolbox h3::before{content:"";position:absolute;left:0;top:1px;width:6px;height:6px;background:var(--gold)}
.toolbox{position:absolute;left:40px;top:33px;width:268px}
.toolbox h3{font-size:7px;font-weight:700;position:relative;padding-left:11px;margin-bottom:1.5px}
.toolbox p{font-size:6.2px;color:var(--grey);line-height:1.35;margin-bottom:6.5px;text-align:justify}
/* bio */
.bio-text{position:absolute;left:49px;top:37px;width:98px;font-size:6.3px;line-height:1.45;color:var(--grey);z-index:1}
.bio-photo{position:absolute;left:152px;top:36px;width:166px;height:176px;background:radial-gradient(ellipse at 35% 55%,#c8a24a 0%,#a98432 45%,#f4f1ea 80%,#fff 100%)}
/* report */
.report{position:absolute;left:40px;top:52px;width:238px;border-collapse:collapse;font-size:6.3px;color:var(--grey)}
.report caption{background:var(--navy);color:#fff;font-weight:700;font-size:9px;height:22px;line-height:22px}
.report td,.report th{border:1px solid #e3e3e8;height:16.6px;text-align:center;font-weight:400}
.report th{font-size:6.2px}
.report .label{font-size:5.2px;line-height:1.05}
.report tr:last-child td{border-bottom:2px solid #b8b8c0}
/* contact */
.contacts{position:absolute;left:0;top:54px;width:318px;text-align:center}
.contact h3{font-size:8.3px;font-weight:700;color:var(--gold);margin-bottom:2px}
.contact p{font-size:6.8px;line-height:1.25}
.divider{width:140px;height:1.5px;margin:5px auto 9px;background:linear-gradient(90deg,transparent,#9a9aa4,transparent)}
/* thank you */
.thanks-brand{position:absolute;left:0;top:56px;width:318px;text-align:center;font-size:16px}
.thanks{position:absolute;left:0;top:138px;width:318px;text-align:center;font:400 19px "Bree Serif",serif;color:var(--gold)}
.thanks-sub{position:absolute;left:0;top:162px;width:318px;text-align:center;font:700 9px "Tinos",serif;color:#111}
</style>
</head>
<body>

<svg width="0" height="0" style="position:absolute">
  <defs>
    <symbol id="footer-band" viewBox="0 0 318 26">
      <path d="M0 17 Q160 15 318 5" fill="none" stroke="#a8894e" stroke-width="1.2"/>
      <path d="M0 20 Q160 18 318 9 L318 26 L0 26 Z" fill="#1b2456"/>
    </symbol>
  </defs>
</svg>

<!-- Cover -->
<section class="slide cover" style="left:90px;top:52px">
  <div class="brand" style="left:20px;top:60px">Ledgerwell Capital Partners</div>
  <div class="cover-title">Company Overview</div>
  <div class="cover-amp">&amp;</div>
  <div class="cover-sub">Marketplace Statistics</div>
  <div class="slide-footer"><svg width="318" height="26"><use href="#footer-band"/></svg><span class="footer-note">Shine a Light on your Treasury Services!</span></div>
</section>

<!-- Contents -->
<section class="slide" style="left:434px;top:52px">
  <h2 class="slide-title" style="left:52px;top:38px">Presentation Contents</h2>
  <ul class="contents">
    <li>LCP’s Toolbox Highlights – page 3</li>
    <li>LCP’s Process – What We Do – pages 4-5</li>
    <li>Clients and References – Who We’ve Helped – pages 6-7</li>
    <li>LCP’s Team – Who We Are and Leadership Bios – pages 8-11</li>
    <li>Treasury Marketplace – pages 12-14</li>
    <li>Service Agreement &amp; Sample Reports – pages 15-18</li>
    <li>Contact Information – page 19</li>
  </ul>
  <div class="slide-footer"><svg width="318" height="26"><use href="#footer-band"/></svg><span class="footer-note">Confidential &amp; Proprietary Information of Ledgerwell Capital Partners</span></div>
</section>

<!-- Toolbox -->
<section class="slide" style="left:783px;top:52px">
  <h2 class="slide-title" style="left:42px;top:8px">LCP’s Toolbox – Highlights</h2>
  <div class="toolbox">
    <h3>LCP’s Goal</h3>
    <p>To provide a “realistic” marketplace comparison of treasury fees, request targeted areas of savings &amp; help our clients navigate bank negotiation</p>
    <h3>LCP’s Value Proposition</h3>
    <p>Treasury savings, solutions and service with LCP broadens our client’s in-house treasury expertise and removes the burden of monthly account analysis reconcilement and error resolution with each contracted bank</p>
    <h3>LCP’s Process</h3>
    <p>Audit treasury &amp; merchant service fees via proprietary &amp; market pricing tools<br>Review each bank’s respective ECR and interest earned to gauge opportunities<br>Survey the banking community for market intelligence unique to each institution<br>Assist with price negotiation &amp; identify back-office improvements<br>Monitor each “master” account analysis statement for accuracy &amp; error</p>
    <h3>LCP’s Team</h3>
    <p>Consortium of ex-bankers with over 100+ years experience</p>
  </div>
  <div class="slide-footer"><svg width="318" height="26"><use href="#footer-band"/></svg><span class="footer-note">Confidential &amp; Proprietary Information of Ledgerwell Capital Partners</span></div>
</section>

<!-- Leadership bio -->
<section class="slide" style="left:264px;top:340px">
  <div class="bio-photo" role="img" aria-label="Photo of a businessman pushing against a tall leaning stack of gold coins"></div>
  <h2 class="slide-title" style="left:49px;top:13px">LCP Leadership Bio</h2>
  <p class="bio-text">Mr. Hale is the developer and creator of LCP’s “four index” pricing system. He is a seasoned veteran in the financial services industry with over 20 years treasury management solutions and bank pricing experience. Mr. Hale is a multi-year Presidential Sales Award winner at both Harborline Bank and Crestmoor Bank, NA. Having managed Fortune 100.</p>
  <div class="slide-footer"><svg width="318" height="26"><use href="#footer-band"/></svg><span class="footer-note">Confidential &amp; Proprietary Information of Ledgerwell Capital Partners</span></div>
</section>

<!-- Sample reports -->
<section class="slide" style="left:608px;top:340px">
  <h2 class="slide-title" style="left:40px;top:14px">Sample Reports - LCP Bank Impact YTD</h2>
  <table class="report">
    <caption>Yearly Recap</caption>
    <tr><th></th><th>Analysis #5070</th><th>Analysis #0572</th><th>Analysis #4120</th></tr>
    <tr><td>Company</td><td>Lorem ipsum</td><td>Lorem ipsum</td><td>Lorem ipsum</td></tr>
    <tr><td>YTD $ Savings</td><td>Lorem ipsum</td><td>Lorem ipsum</td><td>Lorem ipsum</td></tr>
    <tr><td class="label">Proforma $ Savings<br>(Annual)</td><td>Lorem ipsum</td><td>Lorem ipsum</td><td>Lorem ipsum</td></tr>
    <tr><td class="label">YTD Net $ Savings<br>(Less LCP)</td><td>Lorem ipsum</td><td>Lorem ipsum</td><td>Lorem ipsum</td></tr>
    <tr><td class="label">Proforma Net $ Savings<br>(Annual)</td><td>Lorem ipsum</td><td>Lorem ipsum</td><td>Lorem ipsum</td></tr>
    <tr><td>Lorem ipsum</td><td>Lorem ipsum</td><td>Lorem ipsum</td><td>Lorem ipsum</td></tr>
  </table>
  <div class="slide-footer"><svg width="318" height="26"><use href="#footer-band"/></svg><span class="footer-note">Confidential &amp; Proprietary Information of Ledgerwell Capital Partners</span></div>
</section>

<!-- Contact -->
<section class="slide" style="left:264px;top:628px">
  <h2 class="slide-title" style="left:62px;top:20px">LCP Contact Information</h2>
  <div class="contacts">
    <div class="contact">
      <h3>Dorian Hale, Managing Director – Partner, EVP</h3>
      <p>dhale@ledgerwellholdings.example<br>Office 555-014-2200 x 707<br>Cell 555-017-7070</p>
    </div>
    <div class="divider"></div>
    <div class="contact">
      <h3>Miriam Stowe, Managing Director – Partner</h3>
      <p>mstowe@ledgerwellholdings.example<br>Office 555-014-2200 x 706<br>Cell 555-019-0789</p>
    </div>
    <div class="divider"></div>
    <div class="contact">
      <h3>Wendell Pryor, SVP – Sales</h3>
      <p>wpryor@ledgerwellfees.example<br>Office 555-014-2200 x 708<br>Cell 555-016-9519</p>
    </div>
  </div>
  <div class="slide-footer"><svg width="318" height="26"><use href="#footer-band"/></svg><span class="footer-note">Confidential &amp; Proprietary Information of Ledgerwell Capital Partners</span></div>
</section>

<!-- Thank you -->
<section class="slide" style="left:608px;top:628px">
  <div class="brand thanks-brand">Ledgerwell Capital Partners</div>
  <div class="thanks">Thank You!</div>
  <div class="thanks-sub">For your attention</div>
  <div class="slide-footer"><svg width="318" height="26"><use href="#footer-band"/></svg><span class="footer-note">Confidential &amp; Proprietary Information of Ledgerwell Capital Partners</span></div>
</section>

</body>
</html>
```